Home remodeling business card

I would like a business card designed with a play on the word level. I would like the bubble level from a contractors level placed in the o of the word one. I also would like a separate logo done in the corner with just an L and the number 1, rather than the word. I would like the business name in a very bright green, the contact info in a light gray and the business card itself black. I am open to ideas and look forward to seeing your designs
Industry/Entity Type
Business
Contact Information for Business Card
Copper Ridge Home Solutions
Dennis Marlow - Owner
(555)472-3065
Dmw2004@quillmail.com
2963 Harwick Ave
Ashbury Glen VT 05672

```html
<!DOCTYPE html>
<html lang="en">
<head>
<meta charset="utf-8">
<title>Copper Ridge Home Solutions – Business Card</title>
<link rel="stylesheet" href="https://fonts.googleapis.com/css2?family=Open+Sans:wght@400;600&display=swap">
<style>
  :root {
    --page-bg: #2b2b2b;
    --card-black: #0a0a0a;
    --card-sheen: #1c1c1c;
    --brand-green: #8dc63f;
    --text-light: #e6e6e6;
    --text-gray: #bdbdbd;
    --icon-ink: #0a0a0a;
  }
  html, body {
    margin: 0;
    padding: 0;
    width: 1200px;
    height: 849px;
    overflow: hidden;
    background: var(--page-bg);
    font-family: "Open Sans", sans-serif;
  }
  .stage {
    position: relative;
    width: 1200px;
    height: 849px;
    display: flex;
    align-items: center;
    justify-content: center;
    gap: 40px;
  }
  .card {
    position: relative;
    width: 540px;
    height: 309px;
    background: linear-gradient(120deg, var(--card-sheen) 0%, var(--card-black) 45%, var(--card-black) 100%);
    box-shadow: 0 10px 30px rgba(0,0,0,0.55);
    overflow: hidden;
  }
  .accent-bar {
    position: absolute;
    top: 36px;
    bottom: 36px;
    width: 9px;
    background: var(--brand-green);
  }
  .accent-bar--left { left: 12px; }
  .accent-bar--right { right: 12px; }

  /* Front */
  .card-front .brand {
    position: absolute;
    inset: 0;
    display: flex;
    flex-direction: column;
    align-items: center;
    justify-content: center;
    gap: 16px;
  }
  .brand-square {
    width: 40px;
    height: 40px;
    background: var(--brand-green);
  }
  .brand-name {
    color: var(--brand-green);
    font-weight: 400;
    font-size: 24px;
    letter-spacing: 0.2px;
  }

  /* Back */
  .card-back .brand {
    position: absolute;
    top: 40px;
    left: 0;
    right: 0;
    display: flex;
    flex-direction: column;
    align-items: center;
    gap: 12px;
    padding-left: 60px;
  }
  .card-back .brand-square { width: 34px; height: 34px; }
  .card-back .brand-name { font-size: 17px; }

  .contact-block {
    position: absolute;
    top: 166px;
    left: 36px;
    display: flex;
    align-items: stretch;
  }
  .person {
    text-align: right;
    padding-right: 14px;
    padding-top: 2px;
  }
  .person-name {
    color: var(--text-light);
    font-size: 22px;
    line-height: 1.1;
    white-space: nowrap;
  }
  .person-title {
    color: var(--text-gray);
    font-size: 13px;
    margin-top: 4px;
  }
  .divider {
    width: 2px;
    background: var(--brand-green);
  }
  .details {
    list-style: none;
    margin: 0;
    padding: 2px 0 2px 12px;
    display: flex;
    flex-direction: column;
    gap: 5px;
  }
  .detail {
    display: flex;
    align-items: center;
    gap: 8px;
    color: var(--text-gray);
    font-size: 14px;
    line-height: 1;
    white-space: nowrap;
  }
  .detail-icon {
    width: 16px;
    height: 16px;
    flex: none;
  }
</style>
</head>
<body>
<main class="stage">
  <section class="card card-front" aria-label="Card front">
    <span class="accent-bar accent-bar--left"></span>
    <span class="accent-bar accent-bar--right"></span>
    <div class="brand">
      <span class="brand-square"></span>
      <span class="brand-name">Copper Ridge Home Solutions</span>
    </div>
  </section>

  <section class="card card-back" aria-label="Card back">
    <span class="accent-bar accent-bar--left"></span>
    <span class="accent-bar accent-bar--right"></span>
    <div class="brand">
      <span class="brand-square"></span>
      <span class="brand-name">Copper Ridge Home Solutions</span>
    </div>

    <div class="contact-block">
      <div class="person">
        <div class="person-name">Dennis Marlow</div>
        <div class="person-title">Owner</div>
      </div>
      <span class="divider"></span>
      <ul class="details">
        <li class="detail">
          <svg class="detail-icon" viewBox="0 0 16 16" aria-hidden="true">
            <circle cx="8" cy="8" r="8" fill="var(--brand-green)"/>
            <path d="M8 3.5a2.7 2.7 0 0 0-2.7 2.7c0 2 2.7 5.3 2.7 5.3s2.7-3.3 2.7-5.3A2.7 2.7 0 0 0 8 3.5z" fill="var(--icon-ink)"/>
            <circle cx="8" cy="6.2" r="1" fill="var(--brand-green)"/>
          </svg>
          <span>2963 Harwick Ave Ashbury Glen VT 05672</span>
        </li>
        <li class="detail">
          <svg class="detail-icon" viewBox="0 0 16 16" aria-hidden="true">
            <circle cx="8" cy="8" r="8" fill="var(--brand-green)"/>
            <rect x="4" y="5.2" width="8" height="5.6" fill="var(--icon-ink)"/>
            <path d="M4 5.4 8 8.4l4-3" fill="none" stroke="var(--brand-green)" stroke-width="0.9"/>
          </svg>
          <span>Dmw2004@quillmail.com</span>
        </li>
        <li class="detail">
          <svg class="detail-icon" viewBox="0 0 16 16" aria-hidden="true">
            <circle cx="8" cy="8" r="8" fill="var(--brand-green)"/>
            <path d="M5.3 4.2 6.6 4l.8 1.9-.9.8a5 5 0 0 0 2.8 2.8l.8-.9 1.9.8-.2 1.3c-.1.4-.5.7-.9.6A6.5 6.5 0 0 1 4.7 5.1c0-.4.2-.8.6-.9z" fill="var(--icon-ink)"/>
          </svg>
          <span>(555)472-3065</span>
        </li>
      </ul>
    </div>
  </section>
</main>
</body>
</html>
```